Design a Striking Charity Infographic for the Displaced Meal Pledge

Design a striking infographic to share online and raise awareness of the Meal Pledge.

This is a charity project that raises funds to provide refugees with the food, medicine and support they need to survive.

Your design should include the text and ingredients outlined below.

The infographic should be a strong visual statement that’s easy to share on social media such as Picstream, Chirpline and Friendwall.

The headline, ingredients and call to action 'Take the Hope Bridge Meal Pledge, June 19-25'

Text:
Headline: “Could you live on this much food for 1 week?”
Rice 1920g
Flour 400g
Lentils 170g
Dried chick peas 85g
Tinned sardines 125g
Tinned kidney beans 400g
Vegetable Oil 300ml

Take the Hope Bridge Meal Pledge, June 19-25
Sign up at www.mealpledge.example.org.au
(this section with the web address needs to be very clear and easy to see in the graphic)

Footer text - note this section should not dominate, it's a teriary section of the design.
(1) Hope Bridge / Meal Pledge logo
(2) Design by ArtHive (logo attached)

This copy needs to appear somewhere (very small) “The international aid agency of the United Assembly of Parishes. ABN 17 826 305 419”

Technical spec:
Imagery: photos are permitted; custom illustrations encouraged!
Size: maximum 1080x1080px
File size smaller than 5 MB
Colour ratios: Blue and White (80%), tertiary is red; see guide for more details

If the main image is full bleed you can stick headline copy, logos etc on top of it. Put body copy on a grunge brush.

If the images are not full bleed, use a blue background image (rice bag or paper) for the background. Put all the images in a frame. And fasten them on with a fastener (e.g. staple). Make the proportions of the frames / backgrounds / fasteners look realistic.

Logo:
Use the Meal Pledge stamp (larger) and Hope Bridge logo (smaller) on everything. Unless it’s on a plain white background use the sicker version of the HB logo.

Typography:
Veneer 2 for headlines
Caecelia is for body copy in print / on posters / on images put headline and body copy on a grunge brush
Remington Noiseless - use sparingly for personality elements, not for body copy

Pls read the Meal Pledge Visual identity guidelines attached

Background:
From the organizers: "The numbers of refugees are hard to get your head around. And that’s why you taking this challenge is so important.

By putting yourself in the shoes of just one refugee, for just one week, you’re helping to communicate the suffering caused by this crisis on a human level. At a level we, and those around us, can actually understand."

Extra assets:

Frames and fasteners and other assets can be found here: https://files.example-vault.com/s/q9mzt4kx2rbw8ndlpe6vyh3fc17jo5ua

Requirements
Must have
• Refer to the attached visual design guidelines pdf got the colour ratios

```html
<!DOCTYPE html>
<html lang="en">
<head>
<meta charset="utf-8">
<title>Could you live on this much food for 1 week? – Hope Bridge Meal Pledge</title>
<link href="https://fonts.googleapis.com/css2?family=Anton&family=Oswald:wght@600;700&family=Noticia+Text:wght@400;700&display=swap" rel="stylesheet">
<style>
  :root{
    --ink-blue:#1c4a5d;
    --deep-blue:#123847;
    --bg-blue:#21586e;
    --paper:#aac4ce;
    --paper-light:#c5d8de;
    --card:#d3e2e7;
    --card-text:#1f4b5e;
    --red:#8e2733;
    --pin:#d9262f;
    --white:#f4f7f8;
  }
  *{margin:0;padding:0;box-sizing:border-box}
  html,body{width:1199px;height:1200px;overflow:hidden}
  body{
    background:radial-gradient(ellipse at 50% 45%, #2b6780 0%, var(--bg-blue) 45%, var(--deep-blue) 100%);
    font-family:"Noticia Text", Georgia, serif;
    position:relative;
  }
  .headline{
    position:absolute;top:76px;left:0;width:100%;
    text-align:center;
    font-family:"Anton", Impact, sans-serif;font-weight:400;
    font-size:52px;letter-spacing:1.5px;line-height:1.1;
    color:var(--white);
  }
  .torn-paper{position:absolute;top:170px;left:60px;width:1080px;height:880px}
  .ration-card{
    position:absolute;
    background:var(--card);
    border:3px solid var(--red);
    outline:3px solid var(--card);
    color:var(--card-text);
    box-shadow:2px 3px 6px rgba(0,0,0,.25);
  }
  .ration-card .item{
    position:absolute;top:18px;left:22px;
    font-size:26px;white-space:nowrap;
  }
  .ration-card .item.centred{left:0;width:100%;text-align:center}
  .ration-card .amount{
    position:absolute;bottom:12px;left:0;width:100%;text-align:center;
    font-family:"Oswald", "Arial Narrow", sans-serif;font-weight:700;
    font-size:80px;line-height:1;
  }
  .pin{
    position:absolute;top:-14px;right:-14px;width:24px;height:24px;border-radius:50%;
    background:radial-gradient(circle at 35% 35%, #ff5a5f, var(--pin) 55%, #8d1218);
    box-shadow:1px 2px 3px rgba(0,0,0,.35);
  }
  .rice{left:102px;top:270px;width:234px;height:182px;transform:rotate(-3deg)}
  .flour{left:358px;top:268px;width:208px;height:180px;transform:rotate(-2deg)}
  .lentils{left:585px;top:265px;width:196px;height:186px;transform:rotate(-2.5deg)}
  .chickpeas{left:802px;top:252px;width:288px;height:200px;transform:rotate(-3deg)}
  .sardines{left:156px;top:512px;width:276px;height:170px;transform:rotate(2deg)}
  .kidney{left:474px;top:494px;width:328px;height:198px;transform:rotate(3deg)}
  .oil{left:840px;top:494px;width:252px;height:196px;transform:rotate(-3deg)}
  .divider{position:absolute;top:733px;left:112px;width:978px;height:2px;background:rgba(255,255,255,.45)}
  .call-to-action{
    position:absolute;top:752px;left:0;width:100%;text-align:center;
    font-size:33px;color:var(--ink-blue);
  }
  .sign-up{
    position:absolute;top:820px;left:503px;width:194px;height:56px;
    background:var(--red);border-radius:4px;
    font-family:"Anton", Impact, sans-serif;font-size:40px;line-height:56px;
    text-align:center;color:var(--white);letter-spacing:1px;
  }
  .url-band{
    position:absolute;top:914px;left:250px;width:700px;height:70px;
    background:var(--ink-blue);border-radius:30px 10px 34px 12px;transform:rotate(-1deg);
  }
  .url{
    position:absolute;top:922px;left:0;width:100%;text-align:center;
    font-size:38px;color:var(--white);font-weight:700;
  }
  .url .at{font-weight:400}
  .footer-name{
    position:absolute;display:flex;align-items:center;gap:14px;
    font-family:"Noticia Text", Georgia, serif;font-weight:700;
    font-size:30px;color:var(--white);white-space:nowrap;
  }
  .footer-name .mark{width:22px;height:22px;background:var(--white);flex:none}
  .partner-name{top:1072px;left:150px}
  .pledge-name{top:1072px;left:560px}
  .legal{
    position:absolute;top:1140px;left:110px;width:370px;text-align:center;
    font-size:11px;line-height:1.35;color:var(--paper-light);
  }
</style>
</head>
<body>
  <h1 class="headline">COULD YOU LIVE ON THIS MUCH FOOD FOR 1 WEEK ?</h1>

  <svg class="torn-paper" viewBox="0 0 1080 880" aria-hidden="true">
    <polygon fill="var(--paper)" points="12,40 60,30 90,44 140,28 210,36 260,22 330,34 400,20 470,30 540,18 610,32 680,20 760,34 830,22 900,36 960,24 1020,38 1066,30 1072,100 1060,180 1074,260 1062,340 1076,420 1064,500 1074,580 1062,660 1070,740 1058,800 1066,860 990,850 920,864 850,848 780,862 700,852 620,866 540,850 460,864 380,852 300,866 220,852 150,862 80,850 30,858 16,790 28,720 14,640 26,560 12,480 24,400 10,320 22,240 8,160 20,100"/>
  </svg>

  <div class="ration-card rice"><span class="pin"></span><span class="item">Rice</span><span class="amount">1920g</span></div>
  <div class="ration-card flour"><span class="pin"></span><span class="item">Flour</span><span class="amount">400g</span></div>
  <div class="ration-card lentils"><span class="pin"></span><span class="item">Lentils</span><span class="amount">170g</span></div>
  <div class="ration-card chickpeas"><span class="pin"></span><span class="item centred">Dried Chick Peas</span><span class="amount">85g</span></div>
  <div class="ration-card sardines"><span class="pin"></span><span class="item centred">Tinned Sardines</span><span class="amount">125g</span></div>
  <div class="ration-card kidney"><span class="pin"></span><span class="item centred">Tinned Kidney Beans</span><span class="amount">400g</span></div>
  <div class="ration-card oil"><span class="pin"></span><span class="item centred">Vegetable Oil</span><span class="amount">300g</span></div>

  <div class="divider"></div>
  <p class="call-to-action">Take the Hope Bridge Meal Pledge, June 19-25</p>
  <div class="sign-up">SIGN UP</div>
  <div class="url-band"></div>
  <p class="url"><span class="at">at</span> www.mealpledge.example.org.au</p>

  <div class="footer-name partner-name"><span class="mark"></span>Hope Bridge</div>
  <p class="legal">The international aid agency of the United Assembly of Parishes.<br>ABN 17 826 305 419</p>
  <div class="footer-name pledge-name"><span class="mark"></span>Meal Pledge</div>
</body>
</html>
```